Business Card Design Project

I need a business card design for my law office. I already have a logo.

I am an employment attorney who represents clients who have been wrongfully terminated or have been discriminated against by their employer.

I would like a unique, clean design using the colors in the logo or colors that complement the logo.

Target Market(s)

Clients, potential clients, other attorneys and others.

Industry/Entity Type

Attorney

Requirements
Must have
• I would like to use both sides of the card.

The information on the card must be easy to read.

Here is my information:

T. Dale Everhoff
3857 E. Pallister Rd., Suite 204
Fresno, California 93703
559-731-4086
559-862-5143 fax
dale@lawtde.example
Nice to have
• QR Code? I would like to see designs incorporating a nice-looking QR code. Look at this example:

Notice the second QR code in the article - the color.

```html
<!DOCTYPE html>
<html lang="en">
<head>
<meta charset="utf-8">
<title>Everhoff Law Office – Business Card</title>
<link rel="stylesheet" href="https://fonts.googleapis.com/css2?family=EB+Garamond:wght@400;500&display=swap">
<style>
  :root {
    --backdrop: #d9d6d6;
    --card-white: #fbfbfb;
    --brand-blue: #2f8dc0;
    --accent-blue: #1f8ad6;
    --ink-dark: #2a2a2a;
    --ink-grey: #7a7a7a;
    --rule-grey: #cfcfcf;
    --type: "EB Garamond", Georgia, serif;
  }
  * { box-sizing: border-box; margin: 0; padding: 0; }
  html, body { width: 1200px; height: 908px; overflow: hidden; }
  body {
    background: var(--backdrop);
    font-family: var(--type);
    display: flex;
    align-items: center;
    justify-content: center;
    gap: 60px;
  }
  .card {
    width: 540px;
    height: 308px;
    position: relative;
    box-shadow: 0 6px 18px rgba(0,0,0,0.18);
  }

  /* Back side */
  .card--back {
    background: var(--brand-blue);
    display: flex;
    align-items: center;
    justify-content: center;
  }
  .card--back .web {
    color: #ffffff;
    font-size: 34px;
    letter-spacing: 0.5px;
  }

  /* Front side */
  .card--front { background: var(--card-white); }
  .edge-bar {
    position: absolute;
    width: 16px;
    height: 58px;
    background: var(--accent-blue);
  }
  .edge-bar--left { left: 0; top: 112px; }
  .edge-bar--right { right: 0; top: 88px; }

  .holder {
    position: absolute;
    right: 46px;
    top: 44px;
    text-align: right;
  }
  .holder .name {
    font-size: 21px;
    font-weight: 500;
    color: var(--ink-dark);
  }
  .holder .title {
    font-size: 13px;
    color: var(--ink-grey);
    margin-top: 1px;
  }

  .brand {
    position: absolute;
    left: 40px;
    top: 140px;
    display: flex;
    align-items: center;
    gap: 12px;
  }
  .brand .mark {
    width: 34px;
    height: 34px;
    background: var(--accent-blue);
  }
  .brand .brand-name {
    font-size: 25px;
    font-weight: 500;
    color: var(--accent-blue);
    line-height: 1;
  }

  .address {
    position: absolute;
    left: 40px;
    bottom: 36px;
    font-size: 13px;
    line-height: 1.35;
    color: var(--ink-grey);
  }
  .address .web { color: var(--accent-blue); }

  .divider {
    position: absolute;
    left: 300px;
    top: 150px;
    width: 1px;
    height: 70px;
    background: var(--rule-grey);
  }

  .contacts {
    position: absolute;
    left: 318px;
    top: 152px;
    list-style: none;
    font-size: 13px;
    color: var(--ink-grey);
    line-height: 1.5;
  }
  .contacts li { display: flex; align-items: center; gap: 8px; }
  .contacts svg { width: 11px; height: 11px; fill: var(--accent-blue); flex: none; }
</style>
</head>
<body>

  <section class="card card--back" aria-label="Card back">
    <p class="web">www.lawtde.example</p>
  </section>

  <section class="card card--front" aria-label="Card front">
    <span class="edge-bar edge-bar--left"></span>
    <span class="edge-bar edge-bar--right"></span>

    <div class="holder">
      <p class="name">T. Dale Everhoff</p>
      <p class="title">Operation Manager</p>
    </div>

    <div class="brand">
      <span class="mark"></span>
      <span class="brand-name">Everhoff Law Office</span>
    </div>

    <span class="divider"></span>

    <ul class="contacts">
      <li>
        <svg viewBox="0 0 12 12" aria-hidden="true"><path d="M2.4 0.8 4.2 0.5 5.2 3.2 4 4.1a7 7 0 0 0 3.9 3.9l0.9-1.2 2.7 1-0.3 1.8c-0.1 0.6-0.7 1-1.3 0.9C5 9.8 2.2 7 1.5 2.1c-0.1-0.6 0.3-1.2 0.9-1.3z"/></svg>
        559-731-4086
      </li>
      <li>
        <svg viewBox="0 0 12 12" aria-hidden="true"><rect x="3" y="0.5" width="6" height="3"/><rect x="0.5" y="4" width="11" height="5" rx="1"/><rect x="3" y="8" width="6" height="3.5"/></svg>
        559-862-5143
      </li>
      <li>
        <svg viewBox="0 0 12 12" aria-hidden="true"><path d="M0.5 2.5h11v7h-11z M0.5 2.5 6 6.5l5.5-4" fill="none" stroke="#1f8ad6" stroke-width="1.1"/></svg>
        dale@lawtde.example
      </li>
    </ul>

    <div class="address">
      <p>3857 E. Pallister Rd., Suite 204</p>
      <p>Fresno, California 93703</p>
      <p class="web">www.lawtde.example</p>
    </div>
  </section>

</body>
</html>
```